KLW VELVET COMET Party

Hi,
Want to design a flyer for a party.

I have attached a design I would like you to work from and just add in the correct text:

KLW Events presents

November 2013

VELVET COMET
PARTY

DJ MOTH LANTERN
VENUE: TBA

DOORS OPEN 8PM

ENTRY STRICTLY OVER 18'S.

DRESS CODE: SMART CASUAL SULTRY SEXY SPRING THREADS

COST: $60 PER HEAD, includes champagne, beer & wine and canapes.

Tickets from www.marrowquillhub.com.au or 0491 570 158.

```html
<!DOCTYPE html>
<html lang="en">
<head>
<meta charset="utf-8">
<title>KLW Events – Velvet Comet Party</title>
<link rel="stylesheet" href="https://fonts.googleapis.com/css2?family=Open+Sans:wght@700;800&family=Arimo:wght@700&display=swap">
<style>
  :root {
    --pink-light: #f7b6c4;
    --pink-mid: #ec5f7c;
    --red-deep: #d8284f;
    --magenta: #c2206a;
    --ink: #111111;
    --white: #ffffff;
    --band: rgba(255, 255, 255, 0.35);
  }
  * { margin: 0; padding: 0; box-sizing: border-box; }
  html, body { width: 869px; height: 1200px; overflow: hidden; }
  body { background: var(--pink-mid); }
  .flyer {
    position: relative;
    width: 869px;
    height: 1200px;
    overflow: hidden;
    background:
      radial-gradient(circle at 80% 35%, var(--red-deep) 0%, transparent 45%),
      radial-gradient(circle at 70% 90%, var(--magenta) 0%, transparent 55%),
      linear-gradient(160deg, var(--pink-light) 0%, var(--pink-mid) 45%, var(--red-deep) 75%, var(--magenta) 100%);
  }
  .bands { position: absolute; inset: 0; }
  .model-photo {
    position: absolute;
    left: 30px;
    top: 20px;
    width: 420px;
    height: 1180px;
    border-radius: 180px 180px 0 0;
    background: linear-gradient(180deg, #b3305e 0%, #c94a5e 20%, #b52a3d 45%, #2a2124 62%, #e3a79a 78%, #c98b83 100%);
    opacity: 0.85;
  }
  .copy { position: absolute; left: 420px; top: 0; width: 448px; height: 1200px; text-align: center; }
  .line { position: absolute; left: 0; width: 100%; white-space: nowrap; }
  .head { font-family: "Open Sans", Arial, sans-serif; font-weight: 800; color: var(--ink); }
  .info { font-family: "Arimo", Arial, sans-serif; font-weight: 700; color: var(--white); }
  .brand { top: 58px; font-size: 52px; }
  .presents { top: 124px; font-size: 28px; font-weight: 700; }
  .month { top: 181px; font-size: 48px; line-height: 1; }
  .year { top: 236px; font-size: 48px; line-height: 1; }
  .title { top: 333px; font-size: 82px; line-height: 1; }
  .subtitle { top: 436px; font-size: 42px; line-height: 1; }
  .dj { top: 533px; font-size: 30px; line-height: 1; }
  .info-sm { font-size: 21px; line-height: 1; }
  .venue span { background: var(--band); padding: 2px 8px; }
</style>
</head>
<body>
<main class="flyer">
  <svg class="bands" width="869" height="1200" viewBox="0 0 869 1200" aria-hidden="true">
    <rect x="0" y="30" width="869" height="18" fill="rgba(255,255,255,0.3)"/>
    <rect x="0" y="250" width="869" height="14" fill="rgba(255,255,255,0.22)"/>
    <rect x="0" y="300" width="869" height="20" fill="rgba(255,255,255,0.25)"/>
    <rect x="0" y="430" width="869" height="16" fill="rgba(255,255,255,0.2)"/>
    <rect x="455" y="505" width="414" height="18" fill="rgba(255,255,255,0.35)"/>
    <rect x="0" y="580" width="869" height="12" fill="rgba(255,255,255,0.18)"/>
  </svg>

  <div class="model-photo" role="img" aria-label="Photo of a woman with long magenta hair, arms raised, wearing a red and black mini dress"></div>

  <section class="copy">
    <div class="line head brand">KLW Events</div>
    <div class="line head presents">presents</div>
    <div class="line head month">NOVEMBER</div>
    <div class="line head year">2013</div>
    <div class="line head title">VELVET</div>
    <div class="line head subtitle">COMET PARTY</div>
    <div class="line info dj">DJ MOTH LANTERN</div>
    <div class="line info info-sm venue" style="top:604px;"><span>VENUE: TBA</span></div>
    <div class="line info info-sm" style="top:664px;">DOORS OPEN 8PM</div>
    <div class="line info info-sm" style="top:726px;">ENTRY STRICTLY OVER 18'S.</div>
    <div class="line info info-sm" style="top:787px;">DRESS CODE:</div>
    <div class="line info info-sm" style="top:818px;">SMART CASUAL SULTRY</div>
    <div class="line info info-sm" style="top:848px;">SEXY SPRING THREADS</div>
    <div class="line info info-sm" style="top:911px;">COST:</div>
    <div class="line info info-sm" style="top:942px;">$60 PER HEAD,</div>
    <div class="line info info-sm" style="top:972px;">includes champagne,</div>
    <div class="line info info-sm" style="top:1003px;">beer &amp; wine and canapes.</div>
    <div class="line info info-sm" style="top:1065px;">Tickets from</div>
    <div class="line info info-sm" style="top:1096px;">www.marrowquillhub.com.au</div>
    <div class="line info info-sm" style="top:1126px;">or</div>
    <div class="line info info-sm" style="top:1155px;">0491 570 158</div>
  </section>
</main>
</body>
</html>
```